Website for Youth Orchestra to sell tickets and attract young musicians

We are looking for a new website design for a Youth Orchestra; one of the best classical youth orchestras in the county. This project is the design only. <br/><br/>The website serves two main purposes:<br/>• Selling tickets for concerts and performances of the orchestra<br/>• Recruiting young musicians to do audition for the orchestra<br/>
Updates

Need extra days to review

Target Market(s)

Classical music lovers with a special interest in young upcoming musicians.
Young talented musicians

Number of Pages Required

2 page

Colors
ec1f27

Requirements
Must have
• - A Picture on the front page that promotes the main upcomming event
• - Attention for recruiting new musicians
• - Pictures with young musicians (white back ground, see examples)
• - Responsive
• - Please use the logo attached
Should not have
• The brown colors of the current website (kvb-velmorin.example)

```html
<!DOCTYPE html>
<html lang="nl">
<head>
<meta charset="utf-8">
<title>Velmorin Jeugdorkest – Speel mee</title>
<link href="https://fonts.googleapis.com/css2?family=Montserrat:wght@400;500;600;700&display=swap" rel="stylesheet">
<style>
  :root {
    --red: #ec1f27;
    --red-soft: #f28a8e;
    --ink: #1c1c1c;
    --text: #2b2b2b;
    --white: #ffffff;
    --footer-bg: #ffffff;
    --page-bg: #ffffff;
  }
  * { box-sizing: border-box; margin: 0; padding: 0; }
  html, body { width: 922px; height: 1200px; overflow: hidden; }
  body {
    position: relative;
    background: var(--page-bg);
    font-family: "Montserrat", Arial, sans-serif;
    color: var(--text);
  }

  /* Navigation */
  .site-nav {
    position: absolute; left: 0; top: 0; width: 922px; height: 73px;
    display: flex; align-items: center; padding-left: 67px;
  }
  .brand { display: flex; align-items: center; gap: 6px; width: 66px; }
  .brand-mark { width: 44px; height: 44px; border-radius: 50%; background: var(--red); display: flex; align-items: center; justify-content: center; }
  .brand-mark span { color: var(--white); font-size: 7px; font-weight: 700; text-align: center; line-height: 1.1; }
  .nav-links { display: flex; gap: 0; list-style: none; }
  .nav-links li { font-size: 11px; font-weight: 700; color: var(--ink); margin-right: 24px; }
  .nav-links li.is-active { color: var(--red); }

  /* Hero */
  .hero {
    position: absolute; left: 0; top: 73px; width: 922px; height: 403px;
  }
  .hero-photo {
    position: absolute; inset: 0;
    background: linear-gradient(120deg, #7a3a3c 0%, #b56b6e 35%, #8a4446 60%, #c98a8c 100%);
  }
  .hero-card {
    position: absolute; left: 67px; top: 87px; width: 324px; height: 230px;
    background: var(--red); border-radius: 6px; overflow: hidden;
    box-shadow: 0 6px 18px rgba(0,0,0,0.25);
  }
  .hero-card svg { position: absolute; inset: 0; }
  .hero-title {
    position: absolute; top: 62px; left: 0; width: 100%;
    text-align: center; color: var(--white);
    font-size: 23px; font-weight: 700; line-height: 1.2;
  }
  .btn-light {
    position: absolute; left: 100px; top: 140px; width: 125px; height: 24px;
    background: var(--white); color: var(--red);
    font-size: 10px; font-weight: 600; border-radius: 2px;
    display: flex; align-items: center; justify-content: center;
  }

  .scroll-hint {
    position: absolute; top: 484px; left: 0; width: 922px; text-align: center;
    color: var(--red); font-size: 13px; font-weight: 700;
  }
  .scroll-line { position: absolute; left: 460px; top: 507px; width: 2px; height: 72px; background: var(--red-soft); }

  /* Join section */
  .join { position: absolute; left: 67px; top: 598px; width: 345px; }
  .join h2 { font-size: 24px; font-weight: 700; color: var(--ink); margin-bottom: 14px; }
  .join p { font-size: 10px; line-height: 1.32; font-weight: 500; color: var(--text); }
  .btn-primary {
    position: absolute; left: 67px; top: 836px; width: 125px; height: 25px;
    background: var(--red); color: var(--white);
    font-size: 9.5px; font-weight: 600; border-radius: 2px;
    display: flex; align-items: center; justify-content: center;
  }

  .gallery-item { position: absolute; width: 129px; height: 140px; border-radius: 6px; }
  .gallery-a { left: 414px; top: 682px; background: linear-gradient(160deg, #3a3a3a, #15151a 70%); }
  .gallery-b { left: 571px; top: 569px; background: linear-gradient(170deg, #8a7e72, #4a3c30 60%, #2a2220); }
  .gallery-c { left: 726px; top: 682px; background: linear-gradient(180deg, #2a2a2a, #6a6a6a 60%, #3a3a3a); }
  .gallery-d { left: 571px; top: 782px; background: linear-gradient(200deg, #1f3f66, #0f1a2c 60%, #2a2f3a); }

  /* Footer */
  .site-footer {
    position: absolute; left: 0; top: 962px; width: 922px; height: 238px;
    background: var(--footer-bg); box-shadow: 0 -4px 10px rgba(0,0,0,0.05);
  }
  .footer-brand { position: absolute; left: 67px; top: 48px; }
  .contact { position: absolute; left: 133px; top: 50px; font-size: 10px; font-weight: 500; color: var(--ink); list-style: none; }
  .contact li { display: flex; gap: 7px; margin-bottom: 12px; line-height: 1.25; }
  .contact svg { flex: none; margin-top: 1px; }
  .footer-col { position: absolute; top: 50px; list-style: none; font-size: 10px; font-weight: 500; color: var(--ink); }
  .footer-col li { margin-bottom: 7px; }
  .col-1 { left: 332px; } .col-2 { left: 465px; } .col-3 { left: 597px; } .col-4 { left: 730px; }
  .social { position: absolute; top: 178px; left: 399px; display: flex; gap: 22px; list-style: none; }
  .social li { width: 26px; height: 26px; border-radius: 50%; background: var(--red); }
</style>
</head>
<body>

<header class="site-nav">
  <div class="brand"><div class="brand-mark"><span>Velmorin</span></div></div>
  <ul class="nav-links">
    <li>Home</li><li>Orkest</li><li class="is-active">Speel mee</li><li>Concerten</li><li>Tours</li><li>Partners</li><li>Vrienden</li><li>Voormalige leden</li><li>Contacteer &amp; registratie</li>
  </ul>
</header>

<section class="hero">
  <div class="hero-photo" role="img" aria-label="Foto van jonge musici van het orkest die spelen tijdens een concert, met rode overlay"></div>
  <div class="hero-card">
    <svg width="324" height="230" aria-hidden="true">
      <circle cx="160" cy="40" r="30" fill="#fff" fill-opacity="0.12"/>
      <circle cx="210" cy="30" r="22" fill="#fff" fill-opacity="0.1"/>
      <circle cx="255" cy="95" r="28" fill="#fff" fill-opacity="0.1"/>
      <circle cx="240" cy="160" r="20" fill="#fff" fill-opacity="0.1"/>
      <circle cx="110" cy="190" r="26" fill="#fff" fill-opacity="0.08"/>
      <circle cx="200" cy="210" r="18" fill="#fff" fill-opacity="0.08"/>
      <circle cx="60" cy="150" r="14" fill="#fff" fill-opacity="0.07"/>
    </svg>
    <h1 class="hero-title">Wij zijn een team van<br>Unieke leden</h1>
    <div class="btn-light">Join Us</div>
  </div>
</section>

<p class="scroll-hint">Scroll naar beneden om ons team te sluiten</p>
<div class="scroll-line"></div>

<section class="join">
  <h2>Ga nu met ons mee</h2>
  <p>Het Velmorin Youth Orchestra (KVB) is een orkest met<br>
  aantrekkelijke muziek keuzes en frisse ideeën voor de interpretatie<br>
  van concerten en projecten; en niet zonder succes, want op<br>
  de National competition for Youth Symphony Orchestras, voor<br>
  voorbeeld heeft het orkest jarenlang heel goed gescoord.<br>
  De KVB staat dus aan de ene kant voor uitdaging en<br>
  de ontwikkeling van je talent, maar ook voor socialisatie.<br>
  De KVB is een hechte groep jonge muzikanten die genieten<br>
  van het maken vanmuziek samen.<br>
  Bent u geïnteresseerd? Kom dan langs tijdens een repetitie<br>
  om te krijgen en impressie van de sfeer, de muziek en het niveau.<br>
  Het lidmaatschap loopt van 1 september tot 31 augustus, maar u<br>
  ook een interim-lid worden, afhankelijk van de vacatures<br>
  die momenteel beschikbaar zijn. Om lid te worden, vragen we<br>
  potentiële leden om auditie te doen.</p>
</section>
<div class="btn-primary">Book Your Audition</div>

<div class="gallery-item gallery-a" role="img" aria-label="Foto van strijkers in concertkleding van bovenaf"></div>
<div class="gallery-item gallery-b" role="img" aria-label="Foto van het orkest op het podium van een concertzaal"></div>
<div class="gallery-item gallery-c" role="img" aria-label="Foto van een volle concertzaal tijdens een uitvoering"></div>
<div class="gallery-item gallery-d" role="img" aria-label="Foto van een pianist in blauw podiumlicht"></div>

<footer class="site-footer">
  <div class="footer-brand"><div class="brand-mark"><span>Velmorin</span></div></div>
  <ul class="contact">
    <li>
      <svg width="9" height="11" viewBox="0 0 9 11" aria-hidden="true"><path d="M4.5 10.5S1 6.6 1 4.3a3.5 3.5 0 0 1 7 0c0 2.3-3.5 6.2-3.5 6.2z" fill="none" stroke="#ec1f27" stroke-width="1.2"/><circle cx="4.5" cy="4.3" r="1.2" fill="#ec1f27"/></svg>
      <span>Velmorin Jeugdorkest<br>POSTBUS 412<br>4100KV Velmorin</span>
    </li>
    <li>
      <svg width="9" height="10" viewBox="0 0 10 10" aria-hidden="true"><path d="M2 1l2 2-1 1.5c.6 1.2 1.3 1.9 2.5 2.5L7 6l2 2-1.2 1.2C4.5 9 1 5.5.8 2.2z" fill="#ec1f27"/></svg>
      <span>(310) 555-0142</span>
    </li>
    <li>
      <svg width="10" height="8" viewBox="0 0 10 8" aria-hidden="true"><rect x="0.6" y="0.6" width="8.8" height="6.8" fill="none" stroke="#ec1f27" stroke-width="1.1"/><path d="M0.8 1l4.2 3.3L9.2 1" fill="none" stroke="#ec1f27" stroke-width="1.1"/></svg>
      <span>kvb-velmorin.example@mail.com</span>
    </li>
  </ul>
  <ul class="footer-col col-1"><li>Commissies</li><li>Dirigent</li><li>Gedrags code</li><li>Orkestleden</li></ul>
  <ul class="footer-col col-2"><li>Gegevens controleren</li><li>Auditie formulier</li><li>Bezoek repetitie</li><li>Vacatures</li></ul>
  <ul class="footer-col col-3"><li>seizoen 2018-2019</li><li>seizoen 2017-2018</li><li>seizoen 2016-2017</li><li>seizoen 2015-2016</li></ul>
  <ul class="footer-col col-4"><li>Raad</li><li>Contact</li><li>Nieuwsbrief</li><li>Word een vriend</li></ul>
  <ul class="social" aria-label="Sociale media">
    <li aria-label="Sociaal netwerk 1"></li><li aria-label="Sociaal netwerk 2"></li><li aria-label="Videokanaal"></li>
  </ul>
</footer>

</body>
</html>
```